QB-Electronics advertising flag and billboard design

I need a design for advertising flag and a design for billboard.
Information can be obtained from https://qb-elektronik-example.de.
Target Market(s)
IT service for companies
Requirements
Must have
- Logo, contact information and services

```html
<!DOCTYPE html>
<html lang="de">
<head>
<meta charset="utf-8">
<title>QB-Elektronik – Billboard &amp; Flag</title>
<link href="https://fonts.googleapis.com/css2?family=Oswald:wght@400;600&display=swap" rel="stylesheet">
<style>
  :root {
    --brand-blue: #0a0fc8;
    --deep-blue: #0608a8;
    --accent-blue: #1a7de0;
    --line-blue: #2a5fd8;
    --cyan: #45d8f6;
    --panel-white: #f1f2f6;
    --text-grey: #3a3d4a;
    --white: #ffffff;
    --page: #e6e8ee;
  }
  html, body {
    margin: 0;
    padding: 0;
    width: 1200px;
    height: 825px;
    overflow: hidden;
    background: var(--page);
    font-family: "Oswald", "Arial Narrow", sans-serif;
  }
  .artboard {
    position: relative;
    width: 1200px;
    height: 825px;
  }
  .billboard {
    position: absolute;
    left: 30px;
    top: 250px;
    width: 820px;
    height: 323px;
    box-shadow: 0 6px 18px rgba(0,0,0,0.18);
  }
  .billboard svg { display: block; width: 100%; height: 100%; }
  .billboard text { font-family: "Oswald", "Arial Narrow", sans-serif; }
  .flag {
    position: absolute;
    left: 905px;
    top: 50px;
    width: 260px;
    height: 720px;
    background: linear-gradient(160deg, #1530d8 0%, var(--brand-blue) 45%, #1a55e0 80%, #2a7ae8 100%);
    box-shadow: 0 6px 18px rgba(0,0,0,0.18);
    display: flex;
    align-items: center;
    justify-content: center;
  }
  .flag-name {
    writing-mode: vertical-rl;
    transform: rotate(180deg);
    color: var(--cyan);
    font-family: "Oswald", "Arial Narrow", sans-serif;
    font-weight: 600;
    font-size: 86px;
    letter-spacing: 4px;
    line-height: 1;
    margin: 0;
  }
</style>
</head>
<body>
<main class="artboard">

  <section class="billboard" aria-label="QB-Elektronik billboard">
    <svg viewBox="0 0 1320 520" xmlns="http://www.w3.org/2000/svg">
      <defs>
        <linearGradient id="photoTone" x1="0" y1="0" x2="1" y2="1">
          <stop offset="0" stop-color="#e9ecef"/>
          <stop offset="0.55" stop-color="#c9b6a6"/>
          <stop offset="1" stop-color="#4f6b4a"/>
        </linearGradient>
      </defs>

      <rect class="board-bg" x="0" y="0" width="1320" height="520" fill="var(--panel-white)"/>

      <rect class="band-top" x="0" y="0" width="1320" height="34" fill="var(--brand-blue)"/>
      <rect class="band-bottom" x="0" y="486" width="1320" height="34" fill="var(--brand-blue)"/>

      <polygon class="tab-web" points="0,30 500,30 470,112 90,112 62,84 0,84" fill="var(--brand-blue)"/>
      <polygon points="470,112 500,30 520,30 488,112" fill="var(--accent-blue)"/>
      <text x="250" y="88" text-anchor="middle" font-size="34" fill="var(--white)">qb-elektronik-example.de</text>

      <polygon class="tab-mail" points="0,490 500,490 470,414 90,414 62,440 0,440" fill="var(--brand-blue)"/>
      <polygon points="470,414 500,490 520,490 488,414" fill="var(--accent-blue)"/>
      <text x="250" y="470" text-anchor="middle" font-size="34" fill="var(--white)">info@qb-e-example.de</text>

      <text x="250" y="190" text-anchor="middle" font-size="29" fill="var(--text-grey)">SCHNELL &amp; Komfort vor Ort</text>
      <line x1="95" y1="226" x2="405" y2="222" stroke="var(--brand-blue)" stroke-width="2"/>
      <polygon points="185,222 300,220 292,206 196,207" fill="var(--brand-blue)"/>

      <text class="company-name" x="250" y="290" text-anchor="middle" font-size="46" font-weight="600" letter-spacing="3" fill="var(--brand-blue)">QB-ELEKTRONIK</text>

      <line x1="95" y1="330" x2="405" y2="326" stroke="var(--brand-blue)" stroke-width="2"/>
      <polygon points="185,330 300,328 292,343 196,344" fill="var(--brand-blue)"/>

      <text x="250" y="395" text-anchor="middle" font-size="38" fill="var(--brand-blue)">01234-5678900</text>

      <polyline points="410,120 470,150 530,110 700,100" fill="none" stroke="var(--line-blue)" stroke-width="2"/>
      <polyline points="410,400 470,370 530,410 700,420" fill="none" stroke="var(--line-blue)" stroke-width="2"/>
      <circle cx="700" cy="100" r="4" fill="var(--line-blue)"/>
      <circle cx="700" cy="420" r="4" fill="var(--line-blue)"/>

      <polygon class="feature-frame" points="545,60 1320,60 1320,462 545,462 440,261" fill="var(--brand-blue)"/>
      <rect x="1292" y="80" width="28" height="362" fill="var(--panel-white)"/>

      <polygon class="photo" role="img" aria-label="Photo: smiling technician in safety glasses and gloves working on a computer mainboard"
        points="578,82 1045,82 995,261 1045,440 578,440 482,261" fill="url(#photoTone)"/>

      <polygon points="1090,66 1270,66 1250,90 1070,90" fill="var(--accent-blue)"/>
      <polygon points="1090,456 1270,456 1250,432 1070,432" fill="var(--accent-blue)"/>

      <g class="services" font-size="24" fill="var(--white)">
        <text x="1080" y="132">Laptop Reparatur</text>
        <text x="1068" y="166">PC Reparatur</text>
        <text x="1056" y="200">Mac Reparatur</text>
        <text x="1040" y="234">Data Backup and Recovery</text>
        <text x="1028" y="268">Malware and Virus Entfernen</text>
        <text x="1040" y="302">Software Installation</text>
        <text x="1056" y="336">Hardware Upgrade</text>
        <text x="1068" y="370">PC Individuell</text>
        <text x="1080" y="404">Network / Servers</text>
      </g>
    </svg>
  </section>

  <section class="flag" aria-label="QB-Elektronik advertising flag">
    <p class="flag-name">QB-ELEKTRONIK</p>
  </section>

</main>
</body>
</html>
```